Zielgruppe
Branche: Logistik/Spedition
Spezifisch: Fahrzeugüberführung und weitere Dienstleistungen in der Branche siehe Webseite
Zielgruppe: Autohäuser, Leasinggesellschaften, Autovermietungen, Firmen mit eigenem Fuhrpark
Aufgabenstellung
Es handelt sich hierbei um ein Portfolio, welches als E-Mail Anhang an potentielle Kunden zugeschickt oder bei Anfragen per E-Mail mitgeschickt werden soll. Dieses Portfolio wünschen wir in Form einer PDF-Datei.
-Grafische, textliche und inhaltliche Orientierung an unserer Homepage
-alle Dienstleistungen sollen im Portfolio beschrieben werden
-Hauptdienstleistungen, die ausführlicher beschrieben werden sollen: Eigenachsüberfürhung (Hauptdienstleistung)

```html
<!DOCTYPE html>
<html lang="de">
<head>
<meta charset="utf-8">
<title>RELAM – Portfolio Fahrzeugüberführung</title>
<link href="https://fonts.googleapis.com/css2?family=Oswald:wght@500;700&family=Poppins:wght@400;600&display=swap" rel="stylesheet">
<style>
:root{
  --blue:#2c9be3;
  --black:#0b0b0b;
  --grey:#f3f4f5;
  --text:#555a60;
  --line:#e2e4e7;
}
*{box-sizing:border-box;margin:0;padding:0}
html,body{width:1200px;height:4523px;overflow:hidden;background:#fff}
body{position:relative;font-family:'Poppins',sans-serif;color:var(--text)}
.page{position:absolute;left:290px;width:620px;height:438px;background:#fff;overflow:hidden;box-shadow:0 4px 14px rgba(0,0,0,.28)}
.photo{position:absolute}
.band{left:0;top:0;width:620px;height:100px}
.logo-box{position:absolute;right:0;top:0;width:150px;height:100px;background:var(--black);clip-path:polygon(22% 0,100% 0,100% 100%,0 100%)}
.logo-box .name{position:absolute;left:45px;top:22px;font-family:'Oswald',sans-serif;font-weight:700;font-size:24px;color:var(--blue);letter-spacing:1px}
.logo-box .url{position:absolute;left:40px;top:70px;font-size:6.5px;font-weight:600;color:#fff}
.logo-box .url b{color:var(--blue)}
.side-strip{position:absolute;right:0;top:0;width:21px;height:100px;background:var(--blue)}
.col{position:absolute;top:100px;bottom:10px}
.col.left{left:0;width:310px;padding:32px 40px 0 62px}
.col.right{left:310px;right:0;padding:30px 40px 0 28px}
.tint{background:var(--grey)}
.foot{position:absolute;left:0;right:0;bottom:0;height:10px;background:var(--black)}
.foot::after{content:"";position:absolute;right:0;top:0;width:130px;height:10px;background:var(--blue)}
.title{font-family:'Oswald',sans-serif;font-weight:700;font-size:19px;line-height:1.45;color:var(--blue);text-transform:uppercase}
.sub{font-family:'Oswald',sans-serif;font-weight:700;font-size:8px;line-height:1.45;color:var(--black);text-transform:uppercase;margin-bottom:8px}
p{font-size:6px;line-height:1.55;margin-bottom:8px}
.caption{position:absolute;left:61px;top:84px;width:236px;height:54px;background:var(--black);color:#fff;font-weight:600;font-size:8.5px;line-height:1.35;text-align:center;padding-top:12px}
.pic{position:absolute;left:61px;top:238px;width:137px;height:150px}
.ticks{list-style:none}
.ticks li{position:relative;padding-left:15px;font-size:6px;line-height:1.5;margin-bottom:7px}
.ticks li svg{position:absolute;left:0;top:1px;width:8px;height:8px}
.ticks li b{display:block;font-weight:600;color:#333}
.ticks.rule li{border-bottom:1px solid var(--line);padding-bottom:5px;margin-bottom:5px}
.toc{list-style:none}
.toc li{display:flex;justify-content:space-between;font-size:6px;padding:4px 0 4px 22px;border-bottom:1px solid var(--line)}
.step{position:relative;border:1px solid var(--line);background:#fff;padding:8px 10px 8px 36px;margin-bottom:10px}
.step .num{position:absolute;left:9px;top:8px;width:18px;height:18px;background:var(--blue);color:#fff;font-family:'Oswald',sans-serif;font-size:9px;text-align:center;line-height:18px}
.step .sub{margin-bottom:4px}
.step p{margin:0}
</style>
</head>
<body>

<!-- Cover -->
<section class="page" style="top:287px">
  <div class="photo" role="img" aria-label="Foto: lächelnde Fahrerin am Steuer eines Autos" style="left:240px;top:0;width:380px;height:340px;background:linear-gradient(120deg,#5d5f61,#b9b6b0 45%,#3a3b3c)"></div>
  <svg width="620" height="438" style="position:absolute;left:0;top:0">
    <polygon points="0,0 297,0 210,438 0,438" fill="#0b0b0b"/>
    <polygon points="215,412 620,330 620,438 210,438" fill="#fff"/>
    <rect x="485" y="300" width="36" height="40" fill="#fff" stroke="#bbb"/>
    <rect x="525" y="302" width="35" height="36" fill="#ddd"/>
  </svg>
  <div style="position:absolute;left:26px;top:88px;font-family:'Oswald',sans-serif;font-weight:700;font-size:34px;color:var(--blue);letter-spacing:1px">RELAM</div>
  <div style="position:absolute;left:26px;top:168px;font-family:'Oswald',sans-serif;font-weight:700;font-size:22px;line-height:1.35;color:#fff">SIE BRAUCHEN EINE<br>FAHRZEUGÜBERFÜHRUNG?</div>
  <div style="position:absolute;left:26px;top:328px;font-size:5.5px;line-height:1.6;color:#fff;font-weight:600">RELAM GmbH<br><br>Musterallee 12<br>10115 Berlin<br><br>Mo-Fr: 8:00 – 18:00<br>Sa-So: geschlossen</div>
  <div style="position:absolute;left:320px;top:402px;display:flex;gap:22px;font-size:6.5px;font-weight:600;color:#222">
    <span>◎ WWW.RELAM.GMBH</span><span>✉ INFO@RELAM.GMBH</span><span>☏ 030 12 34 56 7-0</span>
  </div>
</section>

<!-- Page 2 -->
<section class="page" style="top:800px">
  <div class="photo band" role="img" aria-label="Foto: Autobahn mit Lkw im Abendlicht" style="background:linear-gradient(90deg,#6c7a4a,#c9a86a 55%,#e0c080)"></div>
  <div class="logo-box"><span class="name">RELAM</span><span class="url">www.relam.gmbh <b>| 2</b></span></div>
  <div class="col left tint">
    <h2 class="title">Fahrzeugüberführung -<br>Unser Service für Ihre<br>Autoüberführung</h2>
    <p style="margin-top:18px">Die RELAM GmbH ist eines der führenden Unternehmen im Bereich Fahrzeugüberführung. Wir führen jährlich mehrere Zehntausend Eigenachsüberführungen durch, sowohl für private als auch für viele namhafte Kunden. Diese Position haben wir uns durch zuverlässige und kundenorientierte Service erarbeitet. Fragen Sie direkt Ihre gewünschten Leistungen an und profitieren Sie von unserer Erfahrung und Expertise.</p>
  </div>
  <div class="col right">
    <div class="sub">Inhalt</div>
    <ul class="toc" style="margin-top:22px">
      <li><span>Eigenachsüberführung</span><span>3</span></li>
      <li><span>Fremdachsenüberführung</span><span>6</span></li>
      <li><span>Stellplätze &amp; Platzdienstleistungen</span><span>7</span></li>
      <li><span>Fahrzeugaufbereitung</span><span>8</span></li>
      <li><span>Reifenhandling</span><span>9</span></li>
      <li><span>Werkstattfahrten</span><span>10</span></li>
      <li><span>Zulassungsdienst</span><span>11</span></li>
      <li><span>Anhängerüberführung</span><span>12</span></li>
      <li><span>Autotransport</span><span>13</span></li>
      <li><span>Fahrzeugtransport</span><span>14</span></li>
    </ul>
  </div>
  <div class="foot"></div>
</section>

<!-- Page 3 -->
<section class="page" style="top:1308px">
  <div class="photo band" role="img" aria-label="Foto: Geländewagen auf Landstraße bei Sonnenuntergang" style="background:linear-gradient(90deg,#8a6a46,#c89860 50%,#5b5d60)"></div>
  <div class="logo-box"><span class="name">RELAM</span><span class="url">www.relam.gmbh <b>| 3</b></span></div>
  <div class="side-strip"></div>
  <div class="col left tint" style="padding-top:80px">
    <h2 class="title">Fahrzeugüberführung<br>auf eigener Achse</h2>
  </div>
  <div class="caption">Zuverlässig ans Ziel<br>mit einer Fahrzeugüberführung<br>vom Experten.</div>
  <div class="photo pic" role="img" aria-label="Foto: Hand mit Smartphone-Navigation im Auto" style="background:linear-gradient(160deg,#8fa4b8,#3d4a58)"></div>
  <div class="col right">
    <div class="sub" style="margin-top:30px">Bundes- und europaweite Überführung von<br>Fahrzeugen durch kompetente Experten</div>
    <p>Die Abholung von Fahrzeugen vom Autohändler, die Überführung von Mietfahrzeugen an einen anderen Unternehmensstandort, der Transport eines besonders wertvollen E-Fahrzeugs: Wann immer ein Fahrzeug sicher überführt werden soll, fehlen oft die zeitlichen oder personellen Ressourcen dafür. Dann benötigen Sie einen zuverlässigen Partner.</p>
    <div class="sub" style="margin-top:14px">Fahrzeugüberführung auf eigener Achse - einfach und<br>sicher mit Unterstützung der RELAM GmbH</div>
    <p>Alle Fahrzeugüberführungen auf eigener Achse werden bei der RELAM GmbH von sorgfältig ausgewählten und eingehend geschulten Mitarbeitern ausgeführt. Wir bieten unseren Service sowohl für zugelassene als auch für nicht zugelassene Fahrzeuge an und überführen diese pünktlich und sicher an den gewünschten Zielort.</p>
  </div>
  <div class="foot"></div>
</section>

<!-- Page 4 -->
<section class="page" style="top:1809px">
  <div class="photo band" role="img" aria-label="Foto: Hände mit Tablet und Dokumenten" style="background:linear-gradient(90deg,#c5cfd8,#8f9aa5 50%,#4c4f53)"></div>
  <div class="logo-box"><span class="name">RELAM</span><span class="url">www.relam.gmbh <b>| 4</b></span></div>
  <div class="side-strip"></div>
  <div class="col left tint" style="padding-top:80px">
    <h2 class="title">Fahrzeugüberführung<br>auf eigener Achse</h2>
  </div>
  <div class="caption">Profitieren Sie<br>mit unserem europaweiten Service<br>zur Autoüberführung.</div>
  <div class="photo pic" role="img" aria-label="Foto: Fahrer vor einem Lkw" style="background:linear-gradient(160deg,#b8c2cc,#6b5a4c)"></div>
  <div class="col right">
    <div class="sub" style="margin-top:5px">Profitieren Sie mit der RELAM von wichtigen Vorteilen</div>
    <ul class="ticks" style="margin-top:10px">
      <li><svg viewBox="0 0 8 8"><rect x=".5" y=".5" width="7" height="7" fill="none" stroke="#2c9be3"/><path d="M2 4l1.5 1.5L6 2.5" fill="none" stroke="#2c9be3"/></svg><b>Transparente Preise</b>Bereits bei Ihrer Anfrage werden Ihnen in Echtzeit die Kosten für die Fahrzeugüberführung angezeigt.</li>
      <li><svg viewBox="0 0 8 8"><rect x=".5" y=".5" width="7" height="7" fill="none" stroke="#2c9be3"/><path d="M2 4l1.5 1.5L6 2.5" fill="none" stroke="#2c9be3"/></svg><b>Zuverlässige Fahrer</b>Für die Eigenachsüberführungen setzen wir erfahrene und regelmäßig geschulte Fahrer ein.</li>
      <li><svg viewBox="0 0 8 8"><rect x=".5" y=".5" width="7" height="7" fill="none" stroke="#2c9be3"/><path d="M2 4l1.5 1.5L6 2.5" fill="none" stroke="#2c9be3"/></svg><b>Langjährige Erfahrung</b>Die RELAM GmbH ist seit vielen Jahren als Dienstleister für Fahrzeugüberführungen am Markt etabliert.</li>
      <li><svg viewBox="0 0 8 8"><rect x=".5" y=".5" width="7" height="7" fill="none" stroke="#2c9be3"/><path d="M2 4l1.5 1.5L6 2.5" fill="none" stroke="#2c9be3"/></svg><b>Eigene App</b>Für noch besseren Service haben wir eine eigene App entwickelt.</li>
      <li><svg viewBox="0 0 8 8"><rect x=".5" y=".5" width="7" height="7" fill="none" stroke="#2c9be3"/><path d="M2 4l1.5 1.5L6 2.5" fill="none" stroke="#2c9be3"/></svg><b>Starkes Kundenportal</b>Mit unserem Kundenportal schaffen wir absolute Transparenz für Ihre Fahrzeugüberführungen auf eigener Achse.</li>
      <li><svg viewBox="0 0 8 8"><rect x=".5" y=".5" width="7" height="7" fill="none" stroke="#2c9be3"/><path d="M2 4l1.5 1.5L6 2.5" fill="none" stroke="#2c9be3"/></svg><b>Fahrzeugzustellungen</b>Fahrzeugzustellungen an den Endnutzer auf Wunsch auch mit Fahrzeugeinweisung.</li>
    </ul>
  </div>
  <div class="foot"></div>
</section>

<!-- Page 5 -->
<section class="page" style="top:2317px">
  <div class="photo band" role="img" aria-label="Foto: Blick aus dem Cockpit auf eine Landstraße" style="background:linear-gradient(90deg,#2b2c2e,#8e9aa6 50%,#b69a6a)"></div>
  <div class="logo-box"><span class="name">RELAM</span><span class="url">www.relam.gmbh <b>| 5</b></span></div>
  <div class="side-strip"></div>
  <div class="col left tint" style="padding-top:80px">
    <h2 class="title">Fahrzeugüberführung<br>auf eigener Achse</h2>
  </div>
  <div class="caption">Die RELAM GmbH überzeugt<br>mit starken Leistungen im Bereich<br>der Fahrzeugüberführung.</div>
  <div class="photo pic" role="img" aria-label="Foto: Hände auf einer Laptop-Tastatur" style="background:linear-gradient(160deg,#e4e2df,#9a8f86)"></div>
  <div class="col right">
    <div class="sub" style="margin-top:25px">Der Ablauf der Fahrzeugüberführungen auf eigener Achse<br>im Überblick</div>
    <div class="step" style="margin-top:12px"><span class="num">01</span><div class="sub">Anfrage &amp; Auftragserteilung</div><p>Stellen Sie einfach eine entsprechende Anfrage über unsere Homepage und erteilen Sie die passende Variante der Fahrzeugüberführung an.</p></div>
    <div class="step"><span class="num">02</span><div class="sub">Fahrzeugübernahme &amp; Zustandsprüfung</div><p>Zum vereinbarten Termin wird das Fahrzeug am angegebenen Ort abgeholt. Unser Mitarbeiter führt eine Zustandsprüfung durch und fertigt eine Übergabeprotokoll an.</p></div>
    <div class="step"><span class="num">03</span><div class="sub">Fahrzeugüberführung &amp; Übergabe</div><p>Ihr Fahrzeug wird auf einer sorgfältig geplanten Route zum Zielort überführt. Die Übergabe erfolgt gemäß der getroffenen Vereinbarungen.</p></div>
  </div>
  <div class="foot"></div>
</section>

<!-- Page 6 -->
<section class="page" style="top:2825px">
  <div class="photo band" role="img" aria-label="Foto: Mitarbeiter prüft ein weißes Auto" style="background:linear-gradient(90deg,#d8dce0,#9aa3ac 50%,#4d5a3e)"></div>
  <div class="logo-box"><span class="name">RELAM</span><span class="url">www.relam.gmbh <b>| 6</b></span></div>
  <div class="side-strip"></div>
  <div class="col left">
    <h2 class="title">Fahrzeugüberführung<br>auf fremder Achse</h2>
    <p style="margin-top:14px">Ob abgemeldet, nicht fahrbereit oder sonderkilometerbeschränkt – Mit unseren Autotransportern bringen wir Ihre Fahrzeuge sicher und zuverlässig ans Ziel. Vor der Beladung wird jedes Fahrzeug durch unsere geschulten Fahrer einer sorgfältigen Zustandsprüfung unterzogen. Der Ist-Zustand wird mithilfe der E-Protokollierung festgehalten und kann jederzeit angeguckt werden.</p>
  </div>
  <div class="col right tint">
    <div class="sub">Profitieren Sie von unseren Leistungen -<br>Fahrzeugüberführung auf fremder Achse</div>
    <ul class="ticks rule" style="margin-top:12px">
      <li><svg viewBox="0 0 8 8"><rect x=".5" y=".5" width="7" height="7" fill="none" stroke="#2c9be3"/><path d="M2 4l1.5 1.5L6 2.5" fill="none" stroke="#2c9be3"/></svg>Überführung von an- und abgemeldeten Fahrzeugen</li>
      <li><svg viewBox="0 0 8 8"><rect x=".5" y=".5" width="7" height="7" fill="none" stroke="#2c9be3"/><path d="M2 4l1.5 1.5L6 2.5" fill="none" stroke="#2c9be3"/></svg>Reichweite: Überführung Deutschland- und Europaweit</li>
      <li><svg viewBox="0 0 8 8"><rect x=".5" y=".5" width="7" height="7" fill="none" stroke="#2c9be3"/><path d="M2 4l1.5 1.5L6 2.5" fill="none" stroke="#2c9be3"/></svg>Zugang zum Kundenportal für absolute Transparenz</li>
      <li><svg viewBox="0 0 8 8"><rect x=".5" y=".5" width="7" height="7" fill="none" stroke="#2c9be3"/><path d="M2 4l1.5 1.5L6 2.5" fill="none" stroke="#2c9be3"/></svg>Neu- und Leasingfahrzeuge</li>
      <li><svg viewBox="0 0 8 8"><rect x=".5" y=".5" width="7" height="7" fill="none" stroke="#2c9be3"/><path d="M2 4l1.5 1.5L6 2.5" fill="none" stroke="#2c9be3"/></svg>Fahrzeugzustellung an den Endnutzer / -einweisung</li>
      <li><svg viewBox="0 0 8 8"><rect x=".5" y=".5" width="7" height="7" fill="none" stroke="#2c9be3"/><path d="M2 4l1.5 1.5L6 2.5" fill="none" stroke="#2c9be3"/></svg>Kurzfristige und flexible Handlungsmöglichkeiten durch schnelle Reaktionszeiten</li>
      <li><svg viewBox="0 0 8 8"><rect x=".5" y=".5" width="7" height="7" fill="none" stroke="#2c9be3"/><path d="M2 4l1.5 1.5L6 2.5" fill="none" stroke="#2c9be3"/></svg>Kompetenter und fachkundige Auskunft über Ihren Auftragsstatus</li>
      <li><svg viewBox="0 0 8 8"><rect x=".5" y=".5" width="7" height="7" fill="none" stroke="#2c9be3"/><path d="M2 4l1.5 1.5L6 2.5" fill="none" stroke="#2c9be3"/></svg>Sicherheit: Ausgebildete sowie erfahrene Fahrer. Auf Wunsch ausgezeichneter Versicherungsschutz durch starke Versicherungspartner</li>
    </ul>
  </div>
  <div class="foot"></div>
</section>

<!-- Page 7 -->
<section class="page" style="top:3332px">
  <div class="photo band" role="img" aria-label="Foto: Parkhaus mit abgestellten Fahrzeugen" style="background:linear-gradient(90deg,#a9b0b8,#e1e4e8 50%,#8f969e)"></div>
  <div class="logo-box"><span class="name">RELAM</span><span class="url">www.relam.gmbh <b>| 7</b></span></div>
  <div class="col left">
    <h2 class="title">Stellplätze &amp;<br>Platzdienstleistungen</h2>
    <p style="margin-top:14px">Mit über 200 überdachten Dauer- oder Tagesstellplätzen bieten wir Ihnen sichere und zentral gelegene Abstellplätze für Ihre Fahrzeuge an. Durch unsere Platzdienstleistungen bieten wir Ihnen den zusätzlichen Service an, Ihre Neu- oder Gebrauchtfahrzeuge in einem unserer Stellplätze zu lagern und abzuholen.</p>
    <p>Bei Anlieferung von Neufahrzeugen wird im Einzelnen und mit Sorgfalt geprüft, ob das Fahrzeug Schäden oder eventuelle Fehlteile aufweist. Auch Gebrauchtfahrzeuge werden auf Beschädigungen oder Verschmutzungen überprüft. Die Bestandsaufnahmen werden durch kompetente Fachkräfte durchgeführt und in einer Dokumentation wie auch einer Checkliste sowohl schriftlich als auch grafisch festgehalten.</p>
  </div>
  <div class="col right tint">
    <div class="sub">Profitieren Sie von unseren Leistungen -<br>Stellplätze &amp; Platzdienstleistungen</div>
    <ul class="ticks rule" style="margin-top:12px">
      <li><svg viewBox="0 0 8 8"><rect x=".5" y=".5" width="7" height="7" fill="none" stroke="#2c9be3"/><path d="M2 4l1.5 1.5L6 2.5" fill="none" stroke="#2c9be3"/></svg>Beauftragung von Instandsetzungen und Wartungen und Bereitstellung einer überdachten Parkfläche</li>
      <li><svg viewBox="0 0 8 8"><rect x=".5" y=".5" width="7" height="7" fill="none" stroke="#2c9be3"/><path d="M2 4l1.5 1.5L6 2.5" fill="none" stroke="#2c9be3"/></svg>Anlieferung und Check-Up von Neu- oder Gebrauchtfahrzeugen zur Prüfung von Zustand und Sicherheit</li>
      <li><svg viewBox="0 0 8 8"><rect x=".5" y=".5" width="7" height="7" fill="none" stroke="#2c9be3"/><path d="M2 4l1.5 1.5L6 2.5" fill="none" stroke="#2c9be3"/></svg>Professioneller, sicherer Hin- und Rücktransport von Fahrzeugen – auch für Hauptuntersuchungen</li>
      <li><svg viewBox="0 0 8 8"><rect x=".5" y=".5" width="7" height="7" fill="none" stroke="#2c9be3"/><path d="M2 4l1.5 1.5L6 2.5" fill="none" stroke="#2c9be3"/></svg>Auslieferung von Neufahrzeugen an den Endnutzer – pünktliche Übergabe ganz nach Kundenwunsch</li>
    </ul>
  </div>
  <div class="foot"></div>
</section>

<!-- Page 8 -->
<section class="page" style="top:3837px">
  <div class="photo band" role="img" aria-label="Foto: Hand poliert ein Auto mit blauem Mikrofasertuch" style="background:linear-gradient(90deg,#3c4046,#8a9098 45%,#4aa3d8 60%,#2c2e31)"></div>
  <div class="logo-box"><span class="name">RELAM</span><span class="url">www.relam.gmbh <b>| 8</b></span></div>
  <div class="col left">
    <h2 class="title">Fahrzeugaufbereitung<br>Rundumsorglospaket</h2>
    <div class="sub" style="margin-top:12px">Unser Angebot für Sie</div>
    <ul class="ticks rule" style="margin-top:8px">
      <li><svg viewBox="0 0 8 8"><rect x=".5" y=".5" width="7" height="7" fill="none" stroke="#2c9be3"/><path d="M2 4l1.5 1.5L6 2.5" fill="none" stroke="#2c9be3"/></svg>Handwäsche inkl. Felgen</li>
      <li><svg viewBox="0 0 8 8"><rect x=".5" y=".5" width="7" height="7" fill="none" stroke="#2c9be3"/><path d="M2 4l1.5 1.5L6 2.5" fill="none" stroke="#2c9be3"/></svg>Basispflege</li>
      <li><svg viewBox="0 0 8 8"><rect x=".5" y=".5" width="7" height="7" fill="none" stroke="#2c9be3"/><path d="M2 4l1.5 1.5L6 2.5" fill="none" stroke="#2c9be3"/></svg>Premiumpflege</li>
      <li><svg viewBox="0 0 8 8"><rect x=".5" y=".5" width="7" height="7" fill="none" stroke="#2c9be3"/><path d="M2 4l1.5 1.5L6 2.5" fill="none" stroke="#2c9be3"/></svg>Basis-Innenraumpflege ohne Außenwäsche</li>
      <li><svg viewBox="0 0 8 8"><rect x=".5" y=".5" width="7" height="7" fill="none" stroke="#2c9be3"/><path d="M2 4l1.5 1.5L6 2.5" fill="none" stroke="#2c9be3"/></svg>Premium-Innenraumpflege ohne Außenwäsche</li>
      <li><svg viewBox="0 0 8 8"><rect x=".5" y=".5" width="7" height="7" fill="none" stroke="#2c9be3"/><path d="M2 4l1.5 1.5L6 2.5" fill="none" stroke="#2c9be3"/></svg>Rundumsorglospaket</li>
      <li><svg viewBox="0 0 8 8"><rect x=".5" y=".5" width="7" height="7" fill="none" stroke="#2c9be3"/><path d="M2 4l1.5 1.5L6 2.5" fill="none" stroke="#2c9be3"/></svg>Lackaufbereitung</li>
      <li><svg viewBox="0 0 8 8"><rect x=".5" y=".5" width="7" height="7" fill="none" stroke="#2c9be3"/><path d="M2 4l1.5 1.5L6 2.5" fill="none" stroke="#2c9be3"/></svg>Leasingrücknahme</li>
    </ul>
  </div>
  <div class="col right tint">
    <div class="sub">Profitieren Sie von unseren Leistungen -<br>Fahrzeugaufbereitung Rundumsorglospaket</div>
    <ul class="ticks rule" style="margin-top:12px">
      <li><svg viewBox="0 0 8 8"><rect x=".5" y=".5" width="7" height="7" fill="none" stroke="#2c9be3"/><path d="M2 4l1.5 1.5L6 2.5" fill="none" stroke="#2c9be3"/></svg>Alle Fahrzeuge, die wir bewegen, sind über uns vollkasko-versichert.</li>
      <li><svg viewBox="0 0 8 8"><rect x=".5" y=".5" width="7" height="7" fill="none" stroke="#2c9be3"/><path d="M2 4l1.5 1.5L6 2.5" fill="none" stroke="#2c9be3"/></svg>Zufriedenheit: Wir sind stets bemüht die Erwartungen aller Kunden zu erfüllen oder gar zu übertreffen.</li>
      <li><svg viewBox="0 0 8 8"><rect x=".5" y=".5" width="7" height="7" fill="none" stroke="#2c9be3"/><path d="M2 4l1.5 1.5L6 2.5" fill="none" stroke="#2c9be3"/></svg>Schnelle Bearbeitung: Optimierte Prozesse ermöglichen eine flexible und schnelle Bearbeitung Ihrer Aufträge.</li>
      <li><svg viewBox="0 0 8 8"><rect x=".5" y=".5" width="7" height="7" fill="none" stroke="#2c9be3"/><path d="M2 4l1.5 1.5L6 2.5" fill="none" stroke="#2c9be3"/></svg>Unser Onlineportal ermöglicht eine komfortable Auftragsvergabe, Protokollierung und Nachverfolgung.</li>
    </ul>
  </div>
  <div class="foot"></div>
</section>

</body>
</html>
```